New Non Profit site design Logo already made
Wren Lane Initiative
N/A
The company will focus on American as well and international politics.
Nothing elegant. We want to appeal to a young crowd..
Modern
Teal
left side
na
We want to appeal to a younger crowd. A crowd that can latch on to what can hope can become a positive movement throughout the world. We have no real guidelines for the site other than we don't want it to be full page site. Keep a white center with a black background surrounding it, be creative is all we ask. Just no login forms.
brightharbor brightharbor
Please focus drafts on ONE of the following and keep in mind that we prefer a simplistic approach to the coding. Helping the community, Helping veterans, making people aware of a certain event going on in the world that the project may want to make a difference in, things of that nature. Thanks to all who participate.
pixelmeadow pixelmeadow
Please upload the logo. thanks
Very simple and easy to build on with basic html and css skills.
Please keep this simple and modern. Our target audience is 18-35 year olds. We don't want a "cartoonish" looking site either.

```html
<!DOCTYPE html>
<html lang="en">
<head>
<meta charset="utf-8">
<title>Wren Lane Initiative</title>
<link href="https://fonts.googleapis.com/css2?family=Ubuntu:ital,wght@0,400;0,500;0,700;1,400&display=swap" rel="stylesheet">
<style>
:root{
  --blue:#0f74c8;
  --blue-dark:#0a62b0;
  --footer-blue:#0a6fc2;
  --ink:#333;
  --muted:#555;
  --panel:#efefef;
  --page:#f5f5f5;
  --line:#dcdcdc;
  --black:#000;
  --nav-top:#5a5a5a;
  --nav-bottom:#2b2b2b;
}
*{margin:0;padding:0;box-sizing:border-box}
html,body{width:1099px;height:1200px;overflow:hidden}
body{background:var(--black);font-family:"Ubuntu",sans-serif;color:var(--ink);position:relative}
a{color:inherit;text-decoration:none}

.masthead{position:absolute;left:0;top:0;width:1099px;height:128px;background:#fff;border-top:3px solid var(--blue)}
.brand{position:absolute;left:128px;top:44px;display:flex;align-items:center;gap:10px}
.brand-mark{width:30px;height:30px;background:var(--blue)}
.brand-name{font-size:24px;font-weight:700;color:var(--blue);letter-spacing:.2px}
.flag-visual{position:absolute;right:0;top:0;width:228px;height:125px;background:linear-gradient(90deg,#fff 0%,#e3e7f0 35%,#efdadc 70%,#eee 100%)}

.main-nav{position:absolute;left:0;top:128px;width:1099px;height:43px;background:linear-gradient(var(--nav-top),var(--nav-bottom))}
.main-nav ul{list-style:none;display:flex;margin-left:120px;height:43px}
.main-nav li{height:43px;display:flex;align-items:center;justify-content:center;color:#fff;font-weight:700;font-size:13px;letter-spacing:.3px;border-right:1px solid #222;box-shadow:1px 0 0 #5e5e5e}
.main-nav li.active{background:var(--blue)}

.page{position:absolute;left:120px;top:171px;width:859px;height:901px;background:var(--page)}

.hero{position:absolute;left:9px;top:9px;width:841px;height:258px;box-shadow:0 10px 10px -6px rgba(0,0,0,.45)}
.hero-panel{position:absolute;left:0;top:0;width:234px;height:258px;background:linear-gradient(#2e3033,#1e1f21);color:#fff}
.hero-panel h1{font-size:17px;font-weight:700;text-align:center;height:50px;line-height:52px;border-bottom:1px solid #111;box-shadow:0 1px 0 #444}
.hero-lead{font-size:12.5px;font-weight:700;color:#ddd;padding:9px 17px 0;line-height:19px}
.hero-text{font-family:Arial,sans-serif;font-size:11.5px;color:#9a9a9a;padding:12px 18px 0;line-height:19.2px}
.hero-btn{display:inline-block;margin:15px 0 0 19px;background:#fff;color:var(--blue);font-weight:700;font-size:12.5px;padding:3px 9px;border-radius:2px}
.hero-pointer{position:absolute;left:234px;top:105px;width:0;height:0;border-top:24px solid transparent;border-bottom:24px solid transparent;border-left:19px solid #242527}
.hero-visual{position:absolute;left:234px;top:0;width:607px;height:258px;background:linear-gradient(100deg,#2b55a6 0%,#3f7fcc 55%,#5c9ad8 100%)}

.politics{position:absolute;left:10px;top:302px;width:516px;height:341px}
.tab-blue{position:absolute;left:0;top:0;width:213px;height:35px;background:linear-gradient(#2b8ee0,var(--blue-dark));color:#fff;font-weight:500;font-size:14px;letter-spacing:.3px;padding:10px 0 0 31px}
.politics-body{position:absolute;left:0;top:35px;width:516px;height:306px;background:var(--panel);border:1px solid var(--line);border-top:2px solid var(--blue);box-shadow:0 1px 2px rgba(0,0,0,.1)}
.politics-body h2{font-size:14.5px;font-weight:700;height:42px;line-height:42px;padding-left:19px;border-bottom:1px solid var(--line);color:#333;background:linear-gradient(#f7f7f7,#ededed)}
.update{position:relative;height:124px;margin:0 18px 0 17px}
.update+.update{border-top:1px solid #d4d4d4}
.update-photo{position:absolute;left:0;top:18px;width:112px;height:86px;background:#fff;padding:4px;box-shadow:0 0 2px rgba(0,0,0,.2)}
.update-photo span{display:block;width:100%;height:100%}
.update-photo .p1{background:linear-gradient(160deg,#8a5a52,#4a4040)}
.update-photo .p2{background:linear-gradient(160deg,#4f6688,#3a3430)}
.update h3{position:absolute;left:124px;top:18px;font-size:14.5px;font-weight:400;color:var(--blue)}
.update p{position:absolute;left:124px;top:42px;width:358px;font-size:11.5px;line-height:19.2px;color:var(--muted)}
.update time{position:absolute;left:2px;top:108px;font-size:12px;font-style:italic;color:var(--blue)}
.update:first-child{height:132px}
.update:first-child .update-photo{top:22px}
.update:first-child h3{top:22px}
.update:first-child p{top:46px}
.update:first-child time{top:112px}

.videos{position:absolute;left:549px;top:302px;width:301px;height:341px}
.tab-light{position:absolute;left:0;top:0;width:80px;height:36px;background:linear-gradient(#fff,#ececec);border:1px solid var(--line);border-bottom:none;font-weight:700;font-size:14.5px;color:#444;text-align:center;line-height:36px;z-index:1}
.videos-body{position:absolute;left:0;top:35px;width:301px;height:306px;background:var(--panel);border:1px solid var(--line);box-shadow:0 1px 2px rgba(0,0,0,.1)}
.player{position:absolute;left:18px;top:16px;width:266px;height:171px;background:#111}
.player-visual{position:absolute;left:0;top:0;width:266px;height:141px;background:linear-gradient(180deg,#5a6070,#2c3550)}
.player-title{position:absolute;left:0;top:0;width:266px;height:25px;background:rgba(0,0,0,.55);color:#fff;font-family:Arial,sans-serif;font-size:11px;padding:7px 10px}
.player-play{position:absolute;left:122px;top:72px;width:30px;height:22px;background:rgba(0,0,0,.75);border-radius:3px}
.player-bar{position:absolute;left:0;top:141px;width:266px;height:30px;background:linear-gradient(#2b2b2b,#111)}
.player-progress{position:absolute;left:0;top:137px;width:266px;height:4px;background:#444}
.player-time{position:absolute;left:78px;top:12px;font-family:Arial,sans-serif;font-size:9.5px;color:#aaa}
.player-time b{color:#fff;font-weight:400}
.select-row{position:absolute;left:19px;top:197px;width:265px;font-size:11.5px;color:#222}
.select-arrows{position:absolute;right:0;top:0;display:flex;gap:1px}
.select-arrows span{width:12px;height:12px;background:#222;border:1px solid #000}
.thumbs{position:absolute;left:18px;top:220px;display:flex;gap:5px}
.thumbs span{width:86px;height:68px}
.t1{background:linear-gradient(#7f93b8,#5a6070)}
.t2{background:linear-gradient(#b8c4d8,#8a7c8a)}
.t3{background:linear-gradient(#3a1a1a,#111)}

.section-head{position:absolute;display:flex;align-items:center;height:33px}
.section-icon{width:33px;height:33px;border-radius:50%;background:var(--blue);box-shadow:inset 0 0 0 3px #cfe3f5}
.section-head h2{font-size:17px;font-weight:400;color:#555;margin:0 9px 0 10px;white-space:nowrap}
.section-head h2 em{font-style:normal;color:var(--blue)}
.section-rule{flex:1;height:8px;background:repeating-linear-gradient(135deg,#c9c9c9 0 2px,#e4e4e4 2px 4px)}
.what-we-do .section-head{left:10px;top:668px;width:515px}
.events .section-head{left:549px;top:668px;width:301px}

.what-text{position:absolute;left:11px;top:709px;width:515px;font-size:11.5px;line-height:19.2px;color:#444}
.read-more{position:absolute;font-family:Arial,sans-serif;font-size:11.5px;color:var(--blue)}
.what-we-do .read-more{left:461px;top:870px}
.events .read-more{left:786px;top:870px}

.event{position:absolute;left:540px;width:302px;height:82px}
.event+.event{border-top:1px solid #ddd}
.event-date{position:absolute;left:0;width:40px;height:36px;background:linear-gradient(#fafafa,#e2e2e2);border:1px solid #d6d6d6;text-align:center;font-weight:700;font-size:12.5px;line-height:15px;padding-top:2px;color:#333}
.event h3{position:absolute;left:50px;font-size:12.5px;font-weight:400;color:var(--blue)}
.event p{position:absolute;left:50px;width:252px;font-size:11.5px;line-height:17.5px;color:#444}
.event-1{top:712px}
.event-1 .event-date,.event-1 h3{top:0}
.event-1 p{top:20px}
.event-2{top:779px}
.event-2 .event-date{top:16px}
.event-2 h3{top:16px}
.event-2 p{top:36px}

.site-footer{position:absolute;left:120px;top:1072px;width:859px;height:128px;background:var(--footer-blue);color:#fff}
.site-footer::before{content:"";position:absolute;left:0;top:0;width:859px;height:8px;background:radial-gradient(ellipse at 50% 0,rgba(0,0,0,.35),transparent 70%)}
.footer-brand{position:absolute;left:10px;top:38px;display:flex;align-items:center;gap:8px}
.footer-brand-mark{width:18px;height:18px;background:#fff}
.footer-brand-name{font-size:17px;font-weight:700;color:#fff}
.footer-nav{position:absolute;right:11px;top:39px;display:flex;font-size:11.5px}
.footer-nav a+a{border-left:1px solid #cfe3f5;margin-left:9px;padding-left:9px}
.footer-legal{position:absolute;right:12px;top:68px;display:flex;font-family:Arial,sans-serif;font-size:10.5px}
.footer-legal a+a{border-left:1px solid #cfe3f5;margin-left:8px;padding-left:8px}
.copyright{position:absolute;left:11px;top:93px;font-size:10.5px}
</style>
</head>
<body>

<header class="masthead">
  <div class="brand"><span class="brand-mark"></span><span class="brand-name">Wren Lane Initiative</span></div>
  <div class="flag-visual" role="img" aria-label="Waving American flag"></div>
</header>

<nav class="main-nav">
  <ul>
    <li class="active" style="width:83px">Home</li>
    <li style="width:84px">About</li>
    <li style="width:79px">News</li>
    <li style="width:88px">Events</li>
    <li style="width:87px">Videos</li>
    <li style="width:156px">American Politics</li>
    <li style="width:182px">International Politics</li>
    <li style="width:96px;border-right:none;box-shadow:none">Contact</li>
  </ul>
</nav>

<main class="page">
  <section class="hero">
    <div class="hero-panel">
      <h1>Lorem ipsum Dolar</h1>
      <p class="hero-lead">Lorem ipsum dolor sit amet, consectetuer.</p>
      <p class="hero-text">Lorem ipsum dolor sit &nbsp;consectetuer adipiscing elitSed ut perspiciat unde omnis iste natus error &nbsp;accusantium doloremque laudantium.</p>
      <a class="hero-btn" href="#">Read More</a>
    </div>
    <div class="hero-pointer"></div>
    <div class="hero-visual" role="img" aria-label="Hero photograph: a person standing on a rock under a blue sky"></div>
  </section>

  <section class="politics">
    <div class="tab-blue">AMERICAN POLITICS</div>
    <div class="politics-body">
      <h2>Recent Updates</h2>
      <article class="update">
        <div class="update-photo"><span class="p1" role="img" aria-label="Campaign rally photo"></span></div>
        <h3>Lorem ipsum dolor sit amet, consectetuer adipiscing.</h3>
        <p>Ut wisi enim ad minim veniam, quis nostrud exerci tation ulla suscipit lobortis nisl ut aliquip ex ea commodo consequat. Duis autem v eum iriure dolor in hendrerit in vulputate velit esse molestie consequat,</p>
        <time>30 Oct 2013</time>
      </article>
      <article class="update">
        <div class="update-photo"><span class="p2" role="img" aria-label="Crowd at a political event"></span></div>
        <h3>Lorem ipsum dolor sit amet, consectetuer adipiscing.</h3>
        <p>Ut wisi enim ad minim veniam, quis nostrud exerci tation ulla suscipit lobortis nisl ut aliquip ex ea commodo consequat. Duis autem v eum iriure dolor in hendrerit in vulputate velit esse molestie consequat,</p>
        <time>28 Oct 2013</time>
      </article>
    </div>
  </section>

  <section class="videos">
    <div class="tab-light">Viedos</div>
    <div class="videos-body">
      <div class="player">
        <div class="player-visual" role="img" aria-label="Video still of politicians at a podium"></div>
        <div class="player-title">American politics</div>
        <div class="player-play">
          <svg width="30" height="22" viewBox="0 0 30 22"><path d="M12 6 L20 11 L12 16 Z" fill="#fff"/></svg>
        </div>
        <div class="player-progress"></div>
        <div class="player-bar">
          <svg width="266" height="30" viewBox="0 0 266 30">
            <path d="M22 9 L32 15 L22 21 Z" fill="#bbb"/>
            <path d="M60 13 H64 L69 9 V21 L64 17 H60 Z" fill="#bbb"/>
            <path d="M72 11 Q75 15 72 19" stroke="#bbb" fill="none"/>
            <path d="M246 10 V8 H249 M256 8 H259 V10 M259 19 V21 H256 M249 21 H246 V19" stroke="#bbb" fill="none"/>
          </svg>
          <span class="player-time"><b>0:00</b> / 7:12</span>
        </div>
      </div>
      <div class="select-row">Select another video:
        <div class="select-arrows">
          <span><svg width="10" height="10" viewBox="0 0 10 10"><path d="M6 2 L3 5 L6 8" stroke="#fff" fill="none"/></svg></span>
          <span><svg width="10" height="10" viewBox="0 0 10 10"><path d="M4 2 L7 5 L4 8" stroke="#fff" fill="none"/></svg></span>
        </div>
      </div>
      <div class="thumbs">
        <span class="t1" role="img" aria-label="Capitol building"></span>
        <span class="t2" role="img" aria-label="Row of international flags"></span>
        <span class="t3" role="img" aria-label="Painted hand on a dark background"></span>
      </div>
    </div>
  </section>

  <section class="what-we-do">
    <div class="section-head"><span class="section-icon"></span><h2>What <em>We Do ?</em></h2><span class="section-rule"></span></div>
    <p class="what-text">Lorem ipsum dolor sit amet, consectetuer adipiscing elit, sed diam nonummy nibh euismo tincidunt ut laoreet dolore magna aliquam erat volutpat. Ut wisi enim ad minim veniam, quis nostrud e tation ullamcorper suscipit lobortis nisl ut aliquip ex ea commodo consequat. Duis autem vel eum iriu dolor in hendrerit in vulputate velit esse molestie consequat, vel illum dolore eu feugiat nulla facilisis at vero eros et accumsan et iusto odio dignissim qui blandit praesent luptatum zzril delenit augue du dolore te feugait nulla facilisi. &nbsp;vel illum dolore eu feugiat nulla facilisis at vero eros et accumsan et iusto odio dignissim qui blandit praesent luptatum.</p>
    <a class="read-more" href="#">Read More »</a>
  </section>

  <section class="events">
    <div class="section-head"><span class="section-icon"></span><h2>Latest <em>Events</em></h2><span class="section-rule"></span></div>
    <article class="event event-1">
      <div class="event-date">30<br>Oct</div>
      <h3>Lorem ipsum dolor &nbsp;sit amet.</h3>
      <p>Ut wisi enim ad minim veniam, quis nostru tation ullamcorper suscipit lobortis.</p>
    </article>
    <article class="event event-2">
      <div class="event-date">30<br>Oct</div>
      <h3>Lorem ipsum dolor &nbsp;sit amet.</h3>
      <p>Ut wisi enim ad minim veniam, quis nostru tation ullamcorper suscipit lobortis.</p>
    </article>
    <a class="read-more" href="#">Read More »</a>
  </section>
</main>

<footer class="site-footer">
  <div class="footer-brand"><span class="footer-brand-mark"></span><span class="footer-brand-name">Wren Lane Initiative</span></div>
  <nav class="footer-nav">
    <a href="#">Home</a><a href="#">About</a><a href="#">American Politics</a><a href="#">International Politics</a><a href="#">News</a><a href="#">Events</a><a href="#">Videos</a><a href="#">Contact</a>
  </nav>
  <div class="footer-legal"><a href="#">Terms of Use</a><a href="#">Privacy Policy</a></div>
  <p class="copyright">© 2013 wrenlaneinitiative.org , All Rights Reserved.</p>
</footer>

</body>
</html>
```